RTW Gourmet Mushrooms web presence and site

The goal is to attract local buyers of fresh mushrooms and to both local and international buyers freeze dried mushrooms. Mushrooms grown will be oyster mushrooms (yellow, pink, blue, king), shiitake, lions main, chestnut, and more. My business will also be selling grow kits that help families who would like to grow there own mushrooms

Target Market(s)

Local restaurants, foodies and people seeking high quality fresh and freeze dried gourmet mushrooms

Coding

Coded - Design and coding required

Number of Pages Required

1 page

Font styles to use
Serif

Requirements
Must have
• Pictures of the various mushrooms grown along with the characteristics of each of the mushrooms. Recipes and cooking tips for the various mushrooms. There needs to be
1. Order forms with online payments
2. Feedback
3. Preorders for mushrooms that may be more seasonal
4.links to social media Facebook, LinkedIn, etc... I am not knowledgeable in this area
5. Contact Us link email, address, phone
6. About Us link explaining Peter Lindqvist & Moira Dunstable and a brief explanation about us and why we became Mushroom farmers
7. Descriptions of the various mushroom varieties grown and how they are best prepared and served
8. Why Freeze Drying mushrooms and the benefits of Freeze Drying over other methods of preservation.
Nice to have
• 1. Recipes and cooking tips for each of the mushrooms.
2. Weekly additional resources added to different pages
3. Q&A section
4. Food Blog with resources added weekly
5.

Flexibility with future expansion and growth is essential. I would like to have a growing site, not a stagnant site.
Should not have
• 1. Boring, bland presentation.
2. The web site is one to educate, promote the various mushrooms grown
3. No music, video or sound on the main pages but eventually a Vlog might be in the works.

I realize there is a lot of content requested but the content needs to attract buyers and to have the site a go to site for foodies

```html
<!DOCTYPE html>
<html lang="en">
<head>
<meta charset="utf-8">
<title>RTW Gourmet Mushrooms</title>
<link href="https://fonts.googleapis.com/css2?family=Poppins:wght@300;400;500;600&display=swap" rel="stylesheet">
<style>
:root{
  --green:#6cb715;
  --green-soft:#cde6a8;
  --navy:#1f2238;
  --ink:#2b2d42;
  --text:#555a66;
  --muted:#8a8f99;
  --page:#f5f6fa;
  --white:#ffffff;
  --star:#f4a300;
  --link:#3f4a8c;
}
*{margin:0;padding:0;box-sizing:border-box}
html,body{width:1200px;height:3034px;overflow:hidden}
body{font-family:'Poppins',sans-serif;color:var(--text);background:var(--page);position:relative}
.abs{position:absolute}
a{color:inherit;text-decoration:none}

/* top bar */
.topbar{left:0;top:0;width:1200px;height:57px;background:var(--white)}
.topbar .contact{left:230px;top:21px;font-size:11px;color:var(--text);display:flex;gap:16px;align-items:center}
.brand{font-weight:500;color:var(--green);line-height:1;text-align:center}
.topbar .brand{left:0;width:1200px;top:8px;font-size:20px;line-height:22px}
.topbar .tools{left:876px;top:20px;display:flex;gap:10px;align-items:center}
.dot-icon{width:11px;height:11px;border-radius:50%;background:var(--ink)}

/* nav */
.nav{left:0;top:57px;width:1200px;height:41px;background:var(--green)}
.nav ul{list-style:none;display:flex;gap:32px;position:absolute;left:236px;top:12px;font-size:12.5px;font-weight:500;color:var(--white)}

/* hero */
.hero{left:0;top:98px;width:1200px;height:433px;background:radial-gradient(ellipse at 55% 40%,#e8e4dc 0,#bdb7a8 14%,#4d5a2c 32%,#2f3c1a 60%,#3a2a1b 100%)}
.hero h1{left:0;width:1200px;top:108px;text-align:center;color:var(--white);font-size:50px;font-weight:500;line-height:58px}
.btn{background:var(--green);color:var(--white);border-radius:20px;font-size:13px;font-weight:500;text-align:center}
.hero .btn{left:526px;top:241px;width:148px;height:36px;line-height:36px}
.hero .dots{left:582px;top:378px;display:flex;gap:7px}
.hero .dots i{width:7px;height:7px;border:1px solid #fff;border-radius:50%}
.hero .dots i.on{background:#fff}
.torn{left:0;top:520px;width:1200px;height:120px}

/* products */
.card{width:210px;height:278px;background:var(--white)}
.card .photo{height:164px}
.card h3{position:absolute;left:18px;top:178px;font-size:13px;font-weight:500;color:var(--ink)}
.card p{position:absolute;left:18px;top:200px;width:160px;font-size:11px;line-height:16px;color:var(--muted)}
.card .order{position:absolute;left:18px;top:249px;font-size:10.5px;font-weight:600;color:var(--ink)}
.card .stars{position:absolute;right:18px;top:247px;font-size:10px;color:var(--star);letter-spacing:1px}
.browse{left:505px;top:1283px;width:189px;height:36px;line-height:36px;box-shadow:0 6px 14px rgba(108,183,21,.3)}

/* banners */
.banner{left:0;width:1200px;height:178px}
.banner .copy{color:var(--white);font-size:25px;line-height:38px}
.banner .btn{height:34px;line-height:34px;width:130px}

/* feedback */
.feedback{left:0;top:1567px;width:1200px;height:374px;background:var(--white)}
.sec-title{left:0;width:1200px;text-align:center;font-size:26px;font-weight:600;color:var(--ink)}
.sec-sub{left:0;width:1200px;text-align:center;font-size:11px;color:var(--text)}
.avatar{border-radius:50%}
.quote{left:0;width:1200px;top:243px;text-align:center;font-size:12.5px;line-height:21px;color:var(--text)}
.who{left:0;width:1200px;top:303px;text-align:center;font-size:12.5px;color:var(--green)}

/* blog */
.post{width:234px}
.post .photo{height:189px;border-radius:3px}
.post .date{position:absolute;left:8px;top:8px;width:42px;height:42px;border-radius:50%;background:var(--white);font-size:8px;font-weight:600;color:var(--ink);text-align:center;line-height:9px;padding-top:12px}
.post .meta{position:absolute;top:212px;font-size:9px;color:var(--link)}
.post h4{position:absolute;top:228px;font-size:14px;font-weight:600;line-height:20px;color:var(--ink)}
.post p{position:absolute;top:276px;font-size:10px;line-height:19px;color:var(--muted)}
.post .more{position:absolute;top:322px;font-size:10.5px;color:var(--link)}

/* footer */
.footer{left:0;top:2695px;width:1200px;height:339px;background:var(--navy);color:#c8cad6}
.footer .brand{text-align:left;font-size:22px;line-height:25px}
.footer h5{font-size:11px;font-weight:500;color:var(--white);letter-spacing:.3px}
.footer ul{list-style:none;font-size:10.5px;line-height:20px}
.footer .small{font-size:9.5px;line-height:17px}
.sub-form{left:703px;top:128px;width:267px;height:28px;border-radius:14px;overflow:hidden;display:flex}
.sub-form span{flex:1;background:var(--white);color:var(--muted);font-size:10px;line-height:28px;padding-left:20px}
.sub-form b{width:90px;background:var(--green);color:var(--white);font-size:11px;font-weight:500;text-align:center;line-height:28px}
.socials{left:708px;top:198px;display:flex;gap:9px}
.socials i{width:8px;height:8px;border-radius:50%;background:#a8abbb}
.footer .rule{left:0;top:260px;width:1200px;height:1px;background:#2c3049}
.copyright{left:0;width:1200px;top:302px;text-align:center;font-size:10.5px}
</style>
</head>
<body>

<header class="topbar abs">
  <div class="contact abs">
    <span style="display:flex;gap:6px;align-items:center">
      <svg width="14" height="10" viewBox="0 0 14 10"><rect x=".5" y=".5" width="13" height="9" fill="none" stroke="#555a66"/><path d="M.5.5 7 6 13.5.5" fill="none" stroke="#555a66"/></svg>
      Email Addrests</span>
    <span>12 5550 142</span>
  </div>
  <div class="brand abs">RTW Gourmet<br>Mushrooms</div>
  <div class="tools abs">
    <svg width="14" height="14" viewBox="0 0 14 14"><circle cx="6" cy="6" r="4.5" fill="none" stroke="#555a66" stroke-width="1.4"/><path d="M9.5 9.5 13 13" stroke="#555a66" stroke-width="1.4"/></svg>
    <span style="width:1px;height:16px;background:#ccc"></span>
    <i class="dot-icon"></i><i class="dot-icon"></i><i class="dot-icon"></i>
  </div>
</header>

<nav class="nav abs">
  <ul>
    <li>Home</li><li>Order Forms</li><li>About Us</li><li>Preorders</li><li>Descriptions</li><li>benefits of Freeze</li><li>Blog</li><li>Contact Us</li>
  </ul>
</nav>

<section class="hero abs" role="img" aria-label="Close-up photo of a white mushroom growing among grass on the forest floor">
  <h1 class="abs">RTW Gourmet<br>Mushrooms</h1>
  <a class="btn abs">Order Now</a>
  <svg class="abs" style="left:108px;top:207px" width="12" height="22" viewBox="0 0 12 22"><path d="M11 1 1 11l10 10" fill="none" stroke="rgba(255,255,255,.5)" stroke-width="1.5"/></svg>
  <svg class="abs" style="left:1080px;top:207px" width="12" height="22" viewBox="0 0 12 22"><path d="M1 1l10 10L1 21" fill="none" stroke="rgba(255,255,255,.5)" stroke-width="1.5"/></svg>
  <div class="dots abs"><i></i><i class="on"></i><i></i></div>
</section>

<svg class="torn abs" viewBox="0 0 1200 120" preserveAspectRatio="none">
  <path d="M0 18 L60 24 L120 14 L190 26 L260 12 L330 22 L400 10 L470 20 L540 8 L610 20 L680 12 L760 24 L840 10 L920 22 L1000 12 L1080 24 L1140 14 L1200 20 V120 H0Z" fill="#ececec"/>
  <path d="M0 60 Q150 30 300 70 T600 60 T900 70 T1200 55 V120 H0Z" fill="#f3f3f3"/>
  <rect y="100" width="1200" height="20" fill="#f5f6fa"/>
</svg>

<main>
  <article class="card abs" style="left:258px;top:661px">
    <div class="photo" role="img" aria-label="Yellow oyster mushrooms in grass" style="background:linear-gradient(160deg,#3e4a18,#c89a2a 50%,#5a4a16)"></div>
    <h3>Yellow Mushrooms</h3><p>Lorem Ipsum is simply dummy text of the printing</p><span class="order">Order Now</span><span class="stars">★★★★☆</span>
  </article>
  <article class="card abs" style="left:495px;top:661px">
    <div class="photo" role="img" aria-label="Pink oyster mushrooms on a wooden board" style="background:linear-gradient(160deg,#8a8378,#e07a5f 50%,#6f6a62)"></div>
    <h3>Pink Mushrooms</h3><p>Lorem Ipsum is simply dummy text of the printing</p><span class="order">Order Now</span><span class="stars">★★★★☆</span>
  </article>
  <article class="card abs" style="left:733px;top:661px">
    <div class="photo" role="img" aria-label="Blue mushroom growing in moss" style="background:linear-gradient(160deg,#2d3a14,#2a56c8 45%,#8aa238)"></div>
    <h3>Blue Mushrooms</h3><p>Lorem Ipsum is simply dummy text of the printing</p><span class="order">Order Now</span><span class="stars">★★★★☆</span>
  </article>
  <article class="card abs" style="left:258px;top:966px">
    <div class="photo" role="img" aria-label="King oyster mushrooms on a lawn" style="background:linear-gradient(160deg,#4e8a2a,#e6ddcc 50%,#5c9a30)"></div>
    <h3>King Mushrooms</h3><p>Lorem Ipsum is simply dummy text of the printing</p><span class="order">Order Now</span><span class="stars">★★★★☆</span>
  </article>
  <article class="card abs" style="left:495px;top:966px">
    <div class="photo" role="img" aria-label="Shiitake mushrooms on a dark table" style="background:linear-gradient(160deg,#3a3531,#7a5a40 50%,#2e2a26)"></div>
    <h3>Shiitake Mushrooms</h3><p>Lorem Ipsum is simply dummy text of the printing</p><span class="order">Order Now</span><span class="stars">★★★★☆</span>
  </article>
  <article class="card abs" style="left:733px;top:966px">
    <div class="photo" role="img" aria-label="Lion's mane mushrooms on a pale background" style="background:linear-gradient(160deg,#eef3e6,#ead7a8 50%,#eef3e6)"></div>
    <h3>Lions Main Mushrooms</h3><p>Lorem Ipsum is simply dummy text of the printing</p><span class="order">Order Now</span><span class="stars">★★★★☆</span>
  </article>
  <a class="btn browse abs">Browse All Mushrooms</a>
</main>

<section class="banner abs" style="top:1389px;background:radial-gradient(ellipse at 62% 30%,#cfcac0 0,#6e6250 18%,#2e2418 50%,#1e1812 100%)" role="img" aria-label="Blurred photo of a mushroom on dark soil">
  <div class="copy abs" style="left:229px;top:46px">Fresh Mushrooms &amp;<br><span style="padding-left:55px">freeze dried mushrooms</span></div>
  <a class="btn abs" style="left:840px;top:70px">Order Now</a>
</section>

<section class="feedback abs">
  <h2 class="sec-title abs" style="top:64px">Feedback</h2>
  <p class="sec-sub abs" style="top:106px">Look at our latest Products Lorem Ipsum is simply dummy text of the printing</p>
  <div class="avatar abs" style="left:497px;top:150px;width:56px;height:56px;background:var(--green-soft)"></div>
  <div class="avatar abs" style="left:566px;top:144px;width:68px;height:68px;background:var(--green)"></div>
  <div class="avatar abs" style="left:648px;top:150px;width:56px;height:56px;background:var(--green-soft)"></div>
  <p class="quote abs">This is due to their excellent service, competitive pricing and customer support.<br>It's throughly refresing to get such a personal touch.</p>
  <p class="who abs">Hanna Vreeland</p>
  <svg class="abs" style="left:205px;top:261px" width="8" height="12" viewBox="0 0 8 12"><path d="M7 1 2 6l5 5" fill="none" stroke="#2b2d42" stroke-width="1.5"/></svg>
  <div class="abs" style="left:970px;top:247px;width:41px;height:41px;border-radius:50%;background:#ececf0"></div>
</section>

<section class="banner abs" style="top:1941px;background:radial-gradient(ellipse at 45% 100%,#cfcac0 0,#4a5a28 20%,#1f3a10 55%,#16240c 100%)" role="img" aria-label="Blurred photo of a mushroom in green grass">
  <div class="copy abs" style="left:268px;top:44px;text-align:center">Recipes and cooking<br>Tips for the various mushrooms</div>
  <a class="btn abs" style="left:846px;top:71px">Click Here</a>
</section>

<section class="blog">
  <p class="sec-sub abs" style="top:2178px">Blog</p>
  <h2 class="sec-title abs" style="top:2196px;font-weight:300">News and &nbsp;<b style="color:var(--green);font-weight:600">Articles</b></h2>
  <p class="sec-sub abs" style="top:2238px">Look at our latest Products Lorem Ipsum is simply dummy text of the printing</p>

  <article class="post abs" style="left:229px;top:2290px">
    <div class="photo" role="img" aria-label="Orange cup mushrooms on a dark log" style="background:linear-gradient(160deg,#2a2420,#d8502a 50%,#1f1a16)"></div>
    <div class="date">30<br>Nov</div>
    <span class="meta">By Admin &nbsp;&nbsp; . &nbsp;&nbsp; 2 Comments</span>
    <h4>Lorem Ipsum is simply dummy text of the printing</h4>
    <p>There are many variations of passages of available but majority have alteration</p>
    <a class="more">Read More</a>
  </article>
  <article class="post abs" style="left:483px;top:2290px">
    <div class="photo" role="img" aria-label="Bowl of mixed wild mushrooms with herbs" style="background:linear-gradient(160deg,#6a4a2a,#c8a060 50%,#4a3420)"></div>
    <div class="date">26<br>Nov</div>
    <span class="meta">By Admin &nbsp;&nbsp; . &nbsp;&nbsp; 2 Comments</span>
    <h4>Lorem Ipsum is simply dummy text of the printing</h4>
    <p>There are many variations of passages of available but majority have alteration</p>
    <a class="more">Read More</a>
  </article>
  <article class="post abs" style="left:736px;top:2290px">
    <div class="photo" role="img" aria-label="Cluster of brown-capped mushrooms on a dark green background" style="background:linear-gradient(160deg,#22302a,#8a4a40 50%,#1a2420)"></div>
    <div class="date">20<br>Nov</div>
    <span class="meta">By Admin &nbsp;&nbsp; . &nbsp;&nbsp; 2 Comments</span>
    <h4>Lorem Ipsum is simply dummy text of the printing</h4>
    <p>There are many variations of passages of available but majority have alteration</p>
    <a class="more">Read More</a>
  </article>
</section>

<footer class="footer abs">
  <div class="brand abs" style="left:229px;top:66px">RTW Gourmet<br>Mushrooms</div>
  <div class="abs" style="left:229px;top:137px;font-size:15px;color:var(--white)">+123 &nbsp;(555-0176)</div>
  <div class="abs small" style="left:229px;top:171px;width:230px"><span style="font-size:11px;color:var(--white)">Contact</span><br>Lorem Ipsum is simply dummy text of the printing and typesetting industry.</div>
  <h5 class="abs" style="left:524px;top:80px">Quick Links</h5>
  <ul class="abs" style="left:524px;top:104px"><li>Home</li><li>Order Form</li><li>About Us</li><li>Preorders</li><li>Blog</li><li>Contact Us</li></ul>
  <h5 class="abs" style="left:702px;top:80px">WRITE TO US</h5>
  <p class="abs small" style="left:702px;top:103px">Provide your email below to subscribe to our newsletter</p>
  <div class="sub-form abs"><span>Email address</span><b>Subscribe</b></div>
  <h5 class="abs" style="left:702px;top:172px;font-size:10px">FOLLOW US</h5>
  <div class="socials abs"><i></i><i></i><i></i><i></i><i></i></div>
  <div class="rule abs"></div>
  <p class="copyright abs">Copyright 2020 RTW Gourmet Mushrooms</p>
</footer>

</body>
</html>
```